Varnek Semi truck

Hello Designers! I represent a truck driving company in need of a design for our new company trucks & trailers (new Brenta, Dalmoor & roadmaster pellora). I want it modern, not too complicated, & eye catching. I will attach the logo, you can incorporate the symbol as part of the design. If desired, "Drive varnek" can be added to the trailer. The trucks & trailers are going to be white.
I want the back door of the trailer to have our logo or drive4varnek.com
The attached picture of the truck is grey and the logo is gold. The trucks are going to be the same but in white, so we will use the blue Varnek Logo. We are also not sure if we want anything on the cab because we don't want it to feel overwhelming. If you have any questions please ask at mirela@varnek.example. We will tip well for the design we pick. Thank you!

Target Market(s)

Drivers on the road

Industry/Entity Type

Truck driving company

Colors
0094D4
00A9DD
6FCCEA
C7EBF8
E9F6FB

Requirements
Must have
• Our website address to be included on the trailer (not in large print, medium-small): www. drivevarnek .com
Nice to have
• Some kind of pattern on the trailer, possibly cab as well.
Should not have
• any other bright colors other then the logo. A simple line is fine but nothing competing with the logo.

```html
<!DOCTYPE html>
<html lang="en">
<head>
<meta charset="utf-8">
<title>Varnek Trailer Livery</title>
<link rel="stylesheet" href="https://fonts.googleapis.com/css2?family=Jost:wght@500;600&display=swap">
<style>
  :root {
    --teal-deep: #1a4d5f;
    --teal-mid: #2d6f82;
    --teal-pattern: #3f8595;
    --teal-accent: #6bbfc4;
    --teal-pale: #a9dcdd;
    --panel-white: #f3f3f3;
    --canvas: #f5f5f5;
  }
  html, body {
    margin: 0;
    padding: 0;
    width: 1200px;
    height: 1100px;
    overflow: hidden;
    background: var(--canvas);
  }
  .livery-sheet {
    position: relative;
    width: 1200px;
    height: 1100px;
  }
  .panel {
    position: absolute;
    display: block;
  }
  .trailer-side-hex { left: 338px; top: 47px; width: 833px; height: 135px; }
  .trailer-side-band { left: 28px; top: 340px; width: 830px; height: 132px; }
  .rear-door-hex { left: 268px; top: 634px; width: 289px; height: 328px; }
  .rear-door-band { left: 758px; top: 634px; width: 289px; height: 328px; }

  .field { fill: var(--teal-deep); }
  .white-zone { fill: var(--panel-white); }
  .hex-rim { stroke: var(--teal-pale); stroke-width: 4; }
  .hex-rim-dark { stroke: var(--teal-mid); stroke-width: 3; }
  .stripe { fill: var(--teal-accent); }
  .brand-mark { fill: var(--teal-deep); }
  .brand-name {
    font-family: "Jost", sans-serif;
    font-weight: 600;
    fill: var(--teal-deep);
  }
  .web-address {
    font-family: "Jost", sans-serif;
    font-weight: 500;
    fill: var(--teal-deep);
  }
</style>
</head>
<body>
<main class="livery-sheet">

  <!-- Trailer side, hexagon plate -->
  <svg class="panel trailer-side-hex" viewBox="0 0 833 135" aria-label="Trailer side with hexagon name plate">
    <defs>
      <linearGradient id="patternLeft" x1="0" x2="1">
        <stop offset="0" stop-color="var(--teal-pattern)"/>
        <stop offset="1" stop-color="var(--teal-deep)"/>
      </linearGradient>
      <linearGradient id="patternRight" x1="1" x2="0">
        <stop offset="0" stop-color="var(--teal-pattern)"/>
        <stop offset="1" stop-color="var(--teal-deep)"/>
      </linearGradient>
      <linearGradient id="patternTop" y1="0" y2="1" x1="0" x2="0">
        <stop offset="0" stop-color="var(--teal-pattern)"/>
        <stop offset="1" stop-color="var(--teal-deep)"/>
      </linearGradient>
      <linearGradient id="patternBottom" y1="1" y2="0" x1="0" x2="0">
        <stop offset="0" stop-color="var(--teal-pattern)"/>
        <stop offset="1" stop-color="var(--teal-deep)"/>
      </linearGradient>
    </defs>
    <rect class="field" width="833" height="135"/>
    <rect role="img" aria-label="Triangle mosaic pattern" width="110" height="135" fill="url(#patternLeft)"/>
    <rect role="img" aria-label="Triangle mosaic pattern" x="723" width="110" height="135" fill="url(#patternRight)"/>
    <polygon class="white-zone hex-rim" points="225,67 229,31 396,6 566,34 565,105 395,129 229,105"/>
    <rect class="brand-mark" x="300" y="50" width="38" height="38"/>
    <text class="brand-name" x="360" y="85" font-size="44">Varnek</text>
  </svg>

  <!-- Trailer side, diagonal band -->
  <svg class="panel trailer-side-band" viewBox="0 0 830 132" aria-label="Trailer side with diagonal band">
    <rect class="field" width="830" height="132"/>
    <rect role="img" aria-label="Triangle mosaic pattern" width="110" height="132" fill="url(#patternLeft)"/>
    <rect role="img" aria-label="Triangle mosaic pattern" x="720" width="110" height="132" fill="url(#patternRight)"/>
    <polygon class="white-zone" points="258,0 678,0 600,132 180,132"/>
    <polygon class="stripe" points="266,0 275,0 197,132 188,132"/>
    <polygon class="stripe" points="280,0 289,0 211,132 202,132"/>
    <polygon class="stripe" points="651,0 660,0 582,132 573,132"/>
    <polygon class="stripe" points="665,0 674,0 596,132 587,132"/>
    <rect class="brand-mark" x="300" y="44" width="38" height="38"/>
    <text class="brand-name" x="360" y="79" font-size="44">Varnek</text>
  </svg>

  <!-- Rear doors, hexagon plate -->
  <svg class="panel rear-door-hex" viewBox="0 0 289 328" aria-label="Rear doors with hexagon plate">
    <rect class="field" width="289" height="328"/>
    <rect role="img" aria-label="Triangle mosaic pattern" width="289" height="90" fill="url(#patternTop)"/>
    <rect role="img" aria-label="Triangle mosaic pattern" y="238" width="289" height="90" fill="url(#patternBottom)"/>
    <polygon class="white-zone hex-rim-dark" points="3,125 146,89 286,137 286,200 146,240 3,194" fill="#ffffff"/>
    <rect class="brand-mark" x="92" y="124" width="22" height="22"/>
    <text class="brand-name" x="122" y="144" font-size="26">Varnek</text>
    <text class="web-address" x="146" y="200" font-size="18" text-anchor="middle">drive4varnek.com</text>
  </svg>

  <!-- Rear doors, horizontal band -->
  <svg class="panel rear-door-band" viewBox="0 0 289 328" aria-label="Rear doors with horizontal band">
    <rect class="field" width="289" height="328"/>
    <rect role="img" aria-label="Triangle mosaic pattern" width="289" height="92" fill="url(#patternTop)"/>
    <rect role="img" aria-label="Triangle mosaic pattern" y="238" width="289" height="90" fill="url(#patternBottom)"/>
    <rect class="white-zone" y="92" width="289" height="146"/>
    <rect class="stripe" y="101" width="289" height="6"/>
    <rect class="stripe" y="112" width="289" height="6"/>
    <rect class="stripe" y="215" width="289" height="6"/>
    <rect class="stripe" y="226" width="289" height="6"/>
    <rect class="brand-mark" x="92" y="132" width="22" height="22"/>
    <text class="brand-name" x="122" y="152" font-size="26">Varnek</text>
    <text class="web-address" x="146" y="198" font-size="18" text-anchor="middle">drive4varnek.com</text>
  </svg>

</main>
</body>
</html>
```